distributor of aftermarket auto electrical components

I am after business card design for my new company called
Coral Vehicle Supplies (CORAL as the acronym). I will supplying automotive wiring components, basically from battery to headlight. I will be aiming to sell in the 4wd scene and to auto electricians. i am not worried which colours are used though i would like it to be dynamic.
Updates

sorry guys, i have add a mobile and e-mail address that will need to on there as well. Sorry for theĀ inconvenience.

sorry guys i had erred on my spelling with my e-mail. i have now fixed it in the brief

Target Market(s)

4wd industry, custom cars, RV, auto electricians

Industry/Entity Type

Electrical

Requirements
Must have
• Company Name
ABN number: 47 316 208 594
Director: Morris Tandy
M 0438 271 954
E mtandyo@bellwire.com.au

```html
<!DOCTYPE html>
<html lang="en">
<head>
<meta charset="utf-8">
<title>Coral Vehicle Supplies — Business Card</title>
<link rel="stylesheet" href="https://fonts.googleapis.com/css2?family=Tinos:wght@400;700&family=Arimo:wght@700&display=swap">
<style>
  :root {
    --backdrop: #c6c6c6;
    --card-black: #000000;
    --card-glow: #3a3a3a;
    --band-grey: #3c3c3c;
    --silver: #c9c9c9;
    --silver-soft: #d6d6d6;
    --white: #ffffff;
    --divider: #3a3a3a;
  }
  * { margin: 0; padding: 0; box-sizing: border-box; }
  html, body {
    width: 1200px;
    height: 960px;
    overflow: hidden;
    background: var(--backdrop);
  }
  .board {
    position: relative;
    width: 1200px;
    height: 960px;
  }
  .card {
    position: absolute;
    width: 666px;
    height: 380px;
    overflow: hidden;
    box-shadow: 0 4px 14px rgba(0, 0, 0, 0.25);
  }
  .card--front {
    left: 81px;
    top: 75px;
    background: radial-gradient(ellipse 60% 75% at 50% 42%, var(--card-glow) 0%, #151515 55%, var(--card-black) 100%);
  }
  .card--back {
    left: 435px;
    top: 497px;
    background: var(--card-black);
  }
  .card__band {
    position: absolute;
    left: 0;
    right: 0;
    bottom: 0;
    height: 19px;
    background: var(--band-grey);
  }
  .brand-mark {
    position: absolute;
    font-family: "Tinos", "Times New Roman", serif;
    font-weight: 700;
    color: var(--silver);
    letter-spacing: 0.04em;
    text-align: center;
    line-height: 1;
    white-space: nowrap;
  }
  .brand-name {
    position: absolute;
    font-family: "Tinos", "Times New Roman", serif;
    font-weight: 400;
    color: var(--silver-soft);
    text-align: center;
    white-space: nowrap;
    line-height: 1;
  }
  .card--front .brand-mark {
    left: 0; right: 0;
    top: 118px;
    font-size: 84px;
  }
  .card--front .brand-name {
    left: 0; right: 0;
    top: 268px;
    font-size: 27px;
  }
  .card--back .brand-mark {
    left: 40px;
    width: 264px;
    top: 140px;
    font-size: 42px;
  }
  .card--back .brand-name {
    left: 40px;
    width: 264px;
    top: 219px;
    font-size: 17px;
  }
  .divider {
    position: absolute;
    left: 328px;
    top: 103px;
    width: 1px;
    height: 151px;
    background: var(--divider);
  }
  .contact {
    position: absolute;
    left: 382px;
    top: 100px;
    color: var(--white);
  }
  .contact__name {
    font-family: "Tinos", "Times New Roman", serif;
    font-weight: 400;
    font-size: 24px;
    color: var(--silver-soft);
    letter-spacing: 0.02em;
    line-height: 1;
  }
  .contact__role {
    font-family: "Arimo", Arial, sans-serif;
    font-weight: 700;
    font-size: 13px;
    margin-top: 6px;
    line-height: 1;
  }
  .contact__list {
    list-style: none;
    margin-top: 25px;
    font-family: "Tinos", "Times New Roman", serif;
    font-weight: 700;
    font-size: 16px;
  }
  .contact__item {
    display: flex;
    align-items: center;
    height: 31px;
  }
  .contact__icon {
    width: 17px;
    height: 17px;
    margin-right: 11px;
    flex: none;
  }
</style>
</head>
<body>
  <main class="board">
    <section class="card card--front" aria-label="Business card front">
      <div class="brand-mark">CORAL</div>
      <div class="brand-name">Coral Vehicle Supplies</div>
    </section>

    <section class="card card--back" aria-label="Business card back">
      <div class="brand-mark">CORAL</div>
      <div class="brand-name">Coral Vehicle Supplies</div>
      <div class="divider"></div>
      <div class="contact">
        <div class="contact__name">MORRIS TANDY</div>
        <div class="contact__role">Director</div>
        <ul class="contact__list">
          <li class="contact__item">ABN: 47 316 208 594</li>
          <li class="contact__item">
            <svg class="contact__icon" viewBox="0 0 17 17" aria-hidden="true">
              <rect x="5" y="2" width="7" height="14" rx="1.2" fill="none" stroke="#ffffff" stroke-width="1.4"/>
              <rect x="6.5" y="4" width="4" height="4" fill="#ffffff"/>
              <line x1="6" y1="0.5" x2="6" y2="2" stroke="#ffffff" stroke-width="1.2"/>
            </svg>
            0438 271 954
          </li>
          <li class="contact__item">
            <svg class="contact__icon" viewBox="0 0 17 17" aria-hidden="true">
              <rect x="1.5" y="5" width="14" height="9" fill="none" stroke="#ffffff" stroke-width="1.4"/>
              <polyline points="1.5,5 8.5,10 15.5,5" fill="none" stroke="#ffffff" stroke-width="1.4"/>
            </svg>
            mtandyo@bellwire.com.au
          </li>
        </ul>
      </div>
      <div class="card__band"></div>
    </section>
  </main>
</body>
</html>
```